Chatterly Now Hiring Post - Automotive Mechanics

1080 x 1080 design Chatterly ad post that we are hiring. Text to include:

We are hiring mechanics to perform suspension, brake, clutch and steering repairs on heavy duty trucks, trailers, busses and motorhomes.
Hourly wages plus performance bonus
Crestpoint Health Alliance Heath Care + Dental
401K + Company Match
Weekly Pay
3:00 pm – 11:00 pm Shift – No Weekends
Stop in anytime at Ridgeline Coil Works 5172 Heron Lane, Saginaw, MI 48601
or call 989-555-0187
email you resume to coilworks@ridgelinecoil.example

Target Market(s)

Automotive mechanics / Technicians

Industry/Entity Type

Automotive

Font styles to use
Sans Serif

Colors
0054AA
0677BA
7BADD7
CADEEF
E8F1F8

Requirements
Must have
• Must include the text, our logo, and picture from our service department file = ridgeline-coil-works-service.jpg
Nice to have
• Something similar to the same Pember Motor repair ad I attached
Should not have
• No images of people. The image that we provided is from our repair shop, we would like that one used.

```html
<!DOCTYPE html>
<html lang="en">
<head>
<meta charset="UTF-8">
<title>Ridgeline Coil Works – We're Hiring Heavy Duty Mechanics</title>
<link rel="stylesheet" href="https://fonts.googleapis.com/css2?family=Anton&family=Oswald:wght@500;600&family=Roboto+Condensed:wght@500;700&display=swap">
<style>
  :root {
    --ink: #000000;
    --white: #ffffff;
    --brand-blue: #0054AA;
    --band-blue: #1459bd;
    --mid-blue: #0677BA;
    --sky: #7BADD7;
    --mist: #CADEEF;
    --photo-light: #5b7fae;
    --photo-mid: #2b4a78;
    --photo-dark: #0d1828;
  }
  * { box-sizing: border-box; margin: 0; padding: 0; }
  html, body { width: 1200px; height: 1200px; overflow: hidden; background: var(--ink); }
  .poster { position: relative; width: 1200px; height: 1200px; background: var(--ink); overflow: hidden; color: var(--white); }

  .shop-photo {
    position: absolute; left: 340px; top: 0; width: 860px; height: 730px;
    background:
      radial-gradient(circle at 78% 50%, var(--photo-light) 0%, var(--photo-mid) 28%, transparent 55%),
      radial-gradient(ellipse at 60% 20%, #6f8fb8 0%, transparent 45%),
      linear-gradient(180deg, var(--photo-mid) 0%, #1a2f4e 60%, var(--photo-dark) 100%);
    -webkit-mask-image: linear-gradient(90deg, transparent 0%, #000 35%), linear-gradient(180deg, #000 70%, transparent 100%);
    -webkit-mask-composite: source-in;
    mask-image: linear-gradient(90deg, transparent 0%, #000 35%), linear-gradient(180deg, #000 70%, transparent 100%);
    mask-composite: intersect;
  }

  .brand { position: absolute; left: 36px; top: 70px; display: flex; align-items: center; gap: 16px; }
  .brand-mark { width: 44px; height: 44px; background: var(--white); }
  .brand-name { font-family: 'Oswald', sans-serif; font-weight: 600; font-size: 44px; letter-spacing: 1px; text-transform: uppercase; color: var(--white); }

  .headline {
    position: absolute; left: 34px; top: 168px;
    font-family: 'Anton', sans-serif; font-size: 236px; line-height: 208px;
    text-transform: uppercase; color: var(--white);
    transform: skewX(-6deg); transform-origin: left bottom;
  }

  .role-banner {
    position: absolute; left: 25px; top: 609px; width: 665px; height: 90px;
    background: var(--brand-blue); clip-path: polygon(2% 0, 100% 0, 98.5% 100%, 0 100%);
    display: flex; align-items: center; padding-left: 30px;
  }
  .role-banner span { font-family: 'Anton', sans-serif; font-size: 60px; color: var(--white); transform: skewX(-6deg); display: inline-block; letter-spacing: 0.5px; }

  .intro {
    position: absolute; left: 28px; top: 733px; width: 620px;
    border-left: 6px solid var(--brand-blue); padding-left: 20px;
    font-family: 'Roboto Condensed', sans-serif; font-weight: 500; font-size: 26.5px; line-height: 35px;
  }

  .shift-box {
    position: absolute; left: 728px; top: 708px; width: 442px; height: 128px;
    background: var(--brand-blue); clip-path: polygon(3% 0, 100% 0, 97% 100%, 0 100%);
    display: flex; align-items: center; padding-left: 20px; gap: 14px;
  }
  .shift-box svg { flex: none; }
  .shift-text { font-family: 'Anton', sans-serif; transform: skewX(-6deg); }
  .shift-hours { font-size: 32px; line-height: 38px; border-bottom: 2px solid var(--white); padding-bottom: 2px; white-space: nowrap; }
  .shift-hours small { font-size: 22px; }
  .shift-days { font-size: 57px; line-height: 62px; white-space: nowrap; }

  .perks { position: absolute; top: 858px; left: 0; width: 1200px; height: 160px; }
  .perk { position: absolute; top: 0; width: 300px; margin-left: -150px; text-align: center; }
  .perk svg { display: block; margin: 0 auto 22px; }
  .perk p { font-family: 'Roboto Condensed', sans-serif; font-weight: 700; font-size: 24px; line-height: 29px; text-transform: uppercase; }

  .contact-band {
    position: absolute; left: 0; top: 1043px; width: 1200px; height: 157px;
    background: var(--band-blue);
  }
  .stop-in { position: absolute; left: 30px; top: 30px; font-family: 'Anton', sans-serif; font-size: 52px; line-height: 56px; text-transform: uppercase; }
  .contact-item { position: absolute; top: 0; height: 157px; display: flex; align-items: center; gap: 17px; }
  .contact-tile { width: 44px; height: 66px; background: var(--white); border-radius: 5px; display: flex; align-items: center; justify-content: center; flex: none; }
  .contact-text { font-family: 'Oswald', sans-serif; font-weight: 600; font-size: 25px; line-height: 32px; text-transform: uppercase; }
  .contact-text .plain { text-transform: none; }
  .contact-text.email { font-size: 22.5px; }
</style>
</head>
<body>
<main class="poster">
  <div class="shop-photo" role="img" aria-label="Photo from the service department: heavy truck axle with brake shoes and air suspension on a shop floor"></div>

  <header class="brand">
    <div class="brand-mark"></div>
    <div class="brand-name">Ridgeline Coil Works</div>
  </header>

  <h1 class="headline">We’re<br>Hiring!</h1>

  <div class="role-banner"><span>HEAVY DUTY MECHANICS</span></div>

  <p class="intro">We are hiring mechanics to perform suspension, brake, clutch and steering repairs on heavy duty trucks, trailers, busses and motorhomes.</p>

  <div class="shift-box">
    <svg width="92" height="92" viewBox="0 0 92 92" aria-hidden="true">
      <circle cx="46" cy="46" r="40" fill="none" stroke="#fff" stroke-width="7"/>
      <path d="M44 24 V50 L60 62" fill="none" stroke="#fff" stroke-width="7" stroke-linecap="round" stroke-linejoin="round"/>
    </svg>
    <div class="shift-text">
      <div class="shift-hours">3:00 <small>PM</small> - 11:00 <small>PM SHIFT</small></div>
      <div class="shift-days">NO WEEKENDS</div>
    </div>
  </div>

  <section class="perks">
    <div class="perk" style="left:158px">
      <svg width="80" height="80" viewBox="0 0 80 80" aria-hidden="true">
        <circle cx="40" cy="40" r="40" fill="var(--brand-blue)"/>
        <text x="40" y="55" text-anchor="middle" font-family="Anton, sans-serif" font-size="44" fill="#000">$</text>
      </svg>
      <p>Hourly wages plus<br>performance bonus</p>
    </div>
    <div class="perk" style="left:522px">
      <svg width="82" height="80" viewBox="0 0 82 80" aria-hidden="true">
        <path d="M6 28 C6 12 20 8 32 12 C40 15 44 15 50 12 C58 9 68 14 68 28 C68 40 62 46 62 60 C62 74 56 78 50 78 H22 C16 78 12 74 12 60 C12 46 6 40 6 28 Z" fill="var(--brand-blue)"/>
        <circle cx="64" cy="18" r="15" fill="var(--brand-blue)" stroke="#000" stroke-width="4"/>
        <path d="M64 10 V26 M56 18 H72" stroke="#000" stroke-width="4"/>
      </svg>
      <p>Crestpoint Health Alliance<br>heath care + dental</p>
    </div>
    <div class="perk" style="left:835px">
      <svg width="84" height="80" viewBox="0 0 84 80" aria-hidden="true">
        <path d="M30 14 A14 14 0 0 1 58 14 V20 H30 Z" fill="var(--brand-blue)"/>
        <rect x="26" y="20" width="36" height="5" fill="var(--brand-blue)"/>
        <circle cx="44" cy="34" r="10" fill="var(--brand-blue)"/>
        <path d="M24 66 C24 52 32 46 44 46 C56 46 64 52 64 66 Z" fill="var(--brand-blue)"/>
        <circle cx="18" cy="62" r="12" fill="none" stroke="var(--brand-blue)" stroke-width="7" stroke-dasharray="5 3"/>
        <circle cx="18" cy="62" r="4" fill="var(--brand-blue)"/>
        <path d="M50 72 L76 50" stroke="var(--brand-blue)" stroke-width="7" stroke-linecap="round"/>
      </svg>
      <p>401K + company<br>match</p>
    </div>
    <div class="perk" style="left:1099px">
      <svg width="80" height="80" viewBox="0 0 80 80" aria-hidden="true">
        <rect x="5" y="10" width="70" height="66" rx="8" fill="none" stroke="var(--brand-blue)" stroke-width="6"/>
        <rect x="5" y="10" width="70" height="14" fill="var(--brand-blue)"/>
        <path d="M22 4 V16 M40 4 V16 M58 4 V16" stroke="var(--brand-blue)" stroke-width="6" stroke-linecap="round"/>
        <text x="40" y="64" text-anchor="middle" font-family="Oswald, sans-serif" font-weight="600" font-size="32" fill="var(--brand-blue)">7</text>
      </svg>
      <p>Weekly pay</p>
    </div>
  </section>

  <footer class="contact-band">
    <div class="stop-in">Stop in<br>anytime</div>

    <div class="contact-item" style="left:224px">
      <div class="contact-tile">
        <svg width="26" height="34" viewBox="0 0 26 34" aria-hidden="true">
          <path d="M13 2 A11 11 0 0 1 24 13 C24 21 13 32 13 32 C13 32 2 21 2 13 A11 11 0 0 1 13 2 Z" fill="none" stroke="var(--band-blue)" stroke-width="3.5"/>
          <circle cx="13" cy="13" r="4" fill="var(--band-blue)"/>
        </svg>
      </div>
      <div class="contact-text">Ridgeline Coil Works<br><span class="plain">5172 Heron Lane,</span><br><span class="plain">Saginaw, MI 48601</span></div>
    </div>

    <div class="contact-item" style="left:551px">
      <div class="contact-tile">
        <svg width="30" height="30" viewBox="0 0 24 24" aria-hidden="true">
          <path d="M6.6 10.8a15.1 15.1 0 0 0 6.6 6.6l2.2-2.2a1 1 0 0 1 1-.25 11.4 11.4 0 0 0 3.6.57 1 1 0 0 1 1 1V20a1 1 0 0 1-1 1A17 17 0 0 1 3 4a1 1 0 0 1 1-1h3.5a1 1 0 0 1 1 1c0 1.25.2 2.45.57 3.57a1 1 0 0 1-.25 1z" fill="var(--band-blue)"/>
        </svg>
      </div>
      <div class="contact-text">Or call<br>989-555-0187</div>
    </div>

    <div class="contact-item" style="left:784px">
      <div class="contact-tile">
        <svg width="32" height="24" viewBox="0 0 32 24" aria-hidden="true">
          <rect x="2" y="2" width="28" height="20" fill="none" stroke="var(--band-blue)" stroke-width="2.5"/>
          <path d="M2 2 L16 14 L30 2 M2 22 L12 11 M30 22 L20 11" fill="none" stroke="var(--band-blue)" stroke-width="2.5"/>
        </svg>
      </div>
      <div class="contact-text email">Email you resume to<br><span class="plain">coilworks@ridgelinecoil.example</span></div>
    </div>
  </footer>
</main>
</body>
</html>
```